Marrow medical spa and wellness

Integrate existing logo and web design (colors and background) into tri fold, single card brochure and business card design. We already have a logo and an idea for our promotional material but we would like someone to bring it together for us! Quenvoraspaandwellness.com. We want to see what a marble background with a faded lily (as seen on our webpage) would look like on brochures and business cards.

```html
<!DOCTYPE html>
<html lang="en">
<head>
<meta charset="utf-8">
<title>Marrow Medical Spa and Wellness – Tri-fold Brochure</title>
<link href="https://fonts.googleapis.com/css2?family=Cinzel:wght@400;600&family=Lora:wght@400;600&family=Montserrat:wght@400;500&display=swap" rel="stylesheet">
<style>
:root{
  --bg:#3b3b3d;
  --gold:#c9a129;
  --gold-light:#e6c54f;
  --gold-dark:#a9831a;
  --marble:#f1f1f0;
  --ink:#1f1f1f;
  --grey-tab:#8a8a8a;
  --white:#ffffff;
  --mint:#cfe9e6;
}
*{box-sizing:border-box;margin:0;padding:0}
html,body{width:868px;height:1200px;overflow:hidden;background:var(--bg)}
body{position:relative;font-family:"Lora",serif;color:var(--ink)}
.sheet{position:absolute;left:14px;width:840px;height:575px;display:flex;box-shadow:0 10px 30px rgba(0,0,0,.45)}
.sheet--outside{top:16px}
.sheet--inside{top:609px}
.panel{position:relative;width:280px;height:100%;overflow:hidden;
  background:
   linear-gradient(125deg,transparent 40%,rgba(200,200,200,.35) 41%,transparent 43%),
   linear-gradient(35deg,transparent 62%,rgba(205,205,205,.3) 63%,transparent 64.5%),
   linear-gradient(160deg,#fafafa,var(--marble) 55%,#e8e8e8);}
.panel + .panel{border-left:1px solid rgba(0,0,0,.06)}
.base-strip{position:absolute;left:0;right:0;bottom:0;height:7px;background:linear-gradient(90deg,var(--gold-dark),var(--gold-light),var(--gold))}
.head-band{position:absolute;left:0;top:0;width:280px;height:130px}
.head-title{position:absolute;left:30px;top:30px;font-family:"Cinzel",serif;color:var(--white);font-size:21px;line-height:1.05;letter-spacing:.5px}
.tab{display:inline-block;font-family:"Cinzel",serif;font-size:9px;color:var(--white);padding:3px 10px}
.tab--gold{background:var(--gold)}
.tab--grey{background:var(--grey-tab)}
.price-head{position:absolute;left:22px;top:128px;right:16px;display:flex;align-items:center}
.price-head .cols{margin-left:auto;display:flex;gap:2px}
.price-head .cols .tab{width:56px;text-align:center;padding:3px 0;font-size:8px;font-family:"Lora",serif;font-style:italic}
.price-list{position:absolute;left:28px;right:18px;top:156px;font-size:9.6px;font-weight:600}
.price-row{display:grid;grid-template-columns:1fr 52px 58px;line-height:13.6px}
.price-row span:first-child{white-space:nowrap}
.price-row span+span{text-align:center}
.price-row.gap{margin-top:8px}
.pill{display:block;background:linear-gradient(90deg,var(--gold-dark),var(--gold-light));color:var(--white);font-family:"Cinzel",serif;font-size:12px;letter-spacing:1px;text-align:center;padding:5px 0;border-radius:14px}
.hours{position:absolute;left:26px;right:26px;bottom:62px;text-align:center}
.hours p{font-family:"Montserrat",sans-serif;font-size:10px;line-height:15px;margin-top:8px}
.social{position:absolute;left:0;right:0;bottom:28px;display:flex;justify-content:center;gap:10px}
.social i{display:block;width:13px;height:13px;border-radius:50%;background:var(--gold)}
.contact{position:absolute;left:20px;right:20px;top:378px;text-align:center;font-family:"Montserrat",sans-serif;font-size:10px;line-height:16px}
.contact .pill{margin-bottom:10px}
.contact svg{width:10px;height:10px;vertical-align:-1px;margin-right:4px;fill:none;stroke:var(--gold);stroke-width:1.6}
.contact .pin{display:block;margin:0 auto 4px;width:14px;height:14px}
.cover-brand{position:absolute;left:0;right:0;top:30px;text-align:center}
.cover-brand .name{font-family:"Cinzel",serif;font-size:34px;color:var(--gold);font-weight:400;letter-spacing:1px}
.cover-brand .dot{display:inline-block;width:10px;height:10px;border-radius:50%;background:var(--gold);margin-left:6px;vertical-align:6px}
.cover-brand .sub{font-family:"Cinzel",serif;font-size:9px;color:var(--gold);letter-spacing:1.5px;margin-top:2px}
.cover-art{position:absolute;left:0;top:0;width:280px;height:575px}
.cover-tag{position:absolute;left:0;right:0;top:450px;text-align:center;font-family:"Cinzel",serif;color:var(--white);font-size:19px;line-height:1.2}
.cover-url{position:absolute;left:40px;right:40px;top:510px;text-align:center;font-family:"Montserrat",sans-serif;font-size:9.5px;color:var(--white);border:1px solid var(--white);border-radius:14px;padding:4px 0}
.inner{position:absolute;left:22px;right:20px;top:24px;font-size:8.6px;line-height:11.4px}
.rate{display:grid;grid-template-columns:92px 1fr;border:1px solid var(--gold);margin-bottom:3px}
.rate .tab{font-size:10px;padding:3px 8px}
.rate b{font-family:"Cinzel",serif;font-size:10px;color:var(--gold-dark);text-align:center;padding-top:3px;font-weight:600}
.fillers{font-family:"Lora",serif;font-weight:600;font-size:9.5px;margin:8px 0 6px}
.needle{display:grid;grid-template-columns:110px 1fr;font-size:8.6px}
.section-tab{display:inline-block;background:var(--gold);color:var(--white);font-family:"Lora",serif;font-style:italic;font-size:11px;padding:2px 14px;margin:10px 0 6px}
.section-tab.small{font-size:8.6px;padding:1px 10px;margin:6px 0 2px}
.item{display:grid;grid-template-columns:1fr 38px;gap:6px;padding:5px 0;border-bottom:1px solid var(--gold-light)}
.item:last-of-type{border-bottom:none}
.price{background:var(--gold);color:var(--white);font-size:8px;text-align:center;height:12px;line-height:12px;align-self:start}
.bar{margin-top:6px}
.bar .pill{font-family:"Lora",serif;font-size:8.6px;letter-spacing:0;border-radius:3px;padding:3px 0;margin-bottom:5px}
.line{display:grid;grid-template-columns:1fr 34px;gap:6px;margin-bottom:2px}
.line .price{margin-top:1px}
.iv-block{display:grid;grid-template-columns:1fr 34px;gap:6px}
.iv-block ul{list-style:none;padding-left:0}
.iv-block li.sub{padding-left:16px}
.two-col{display:grid;grid-template-columns:1.2fr 1fr;gap:4px}
.two-col li{white-space:nowrap}
</style>
</head>
<body>

<section class="sheet sheet--outside">

  <article class="panel panel--women">
    <svg class="head-band" viewBox="0 0 280 130" aria-hidden="true">
      <defs><linearGradient id="gb1" x1="0" x2="1"><stop offset="0" stop-color="#b8901f"/><stop offset="1" stop-color="#e6c54f"/></linearGradient></defs>
      <path d="M0 0H280V66Q150 92 0 120Z" fill="url(#gb1)"/>
    </svg>
    <h2 class="head-title">Laser<br>Hair Removal</h2>
    <div class="price-head"><span class="tab tab--gold">Women</span><span class="cols"><span class="tab tab--grey">Individual</span><span class="tab tab--grey">Package of 6</span></span></div>
    <div class="price-list">
      <div class="price-row"><span>Forehead</span><span>$55</span><span>$297</span></div>
      <div class="price-row"><span>Upper Lip</span><span>$40</span><span>$216</span></div>
      <div class="price-row"><span>Cheeks/Sideburns</span><span>$65</span><span>$351</span></div>
      <div class="price-row"><span>Chin</span><span>$40</span><span>$216</span></div>
      <div class="price-row"><span>Neck</span><span>$90</span><span>$486</span></div>
      <div class="price-row"><span>Full Face</span><span>$150</span><span>$810</span></div>
      <div class="price-row"><span>Back of neck</span><span>$65</span><span>$351</span></div>
      <div class="price-row gap"><span>Under Arm</span><span>$65</span><span>$351</span></div>
      <div class="price-row"><span>Half Arm</span><span>$75</span><span>$405</span></div>
      <div class="price-row"><span>Full Arm</span><span>$150</span><span>$810</span></div>
      <div class="price-row"><span>Belly</span><span>$140</span><span>$756</span></div>
      <div class="price-row"><span>Bikini</span><span>$80</span><span>$432</span></div>
      <div class="price-row"><span>Brazilian Bikini</span><span>$140</span><span>$756</span></div>
      <div class="price-row"><span>Half Leg</span><span>$100</span><span>$540</span></div>
      <div class="price-row"><span>Full Leg</span><span>$175</span><span>$945</span></div>
      <div class="price-row"><span>Areola</span><span>$30</span><span>$162</span></div>
    </div>
    <div class="hours">
      <span class="pill">Hours of Operation</span>
      <p>Monday - Saturday 10 AM to 7 PM<br>Sunday by appointment only</p>
    </div>
    <div class="social" aria-label="Social media"><i></i><i></i><i></i></div>
    <div class="base-strip"></div>
  </article>

  <article class="panel panel--men">
    <svg class="head-band" viewBox="0 0 280 130" aria-hidden="true">
      <defs><linearGradient id="gb2" x1="0" x2="1"><stop offset="0" stop-color="#c29a24"/><stop offset="1" stop-color="#e6c54f"/></linearGradient></defs>
      <path d="M0 0H280V92Q150 78 0 108Z" fill="url(#gb2)"/>
    </svg>
    <h2 class="head-title">Laser<br>Hair Removal</h2>
    <div class="price-head" style="top:118px"><span class="tab tab--gold">Men</span><span class="cols"><span class="tab tab--grey">Individual</span><span class="tab tab--grey">Package of 6</span></span></div>
    <div class="price-list" style="top:146px">
      <div class="price-row"><span>Full Beard</span><span>$155</span><span>$810</span></div>
      <div class="price-row"><span>Ears</span><span>$30</span><span>$162</span></div>
      <div class="price-row"><span>Upper Back</span><span>$80</span><span>$432</span></div>
      <div class="price-row"><span>Lower Back</span><span>$80</span><span>$432</span></div>
      <div class="price-row"><span>Upper Chest</span><span>$80</span><span>$432</span></div>
      <div class="price-row"><span>Chest/Abdomen</span><span>$160</span><span>$864</span></div>
      <div class="price-row"><span>Shoulders</span><span>$80</span><span>$432</span></div>
      <div class="price-row gap"><span>Full Back with Shoulders</span><span>$200</span><span>$1080</span></div>
      <div class="price-row"><span>Lower Arms</span><span>$80</span><span>$432</span></div>
      <div class="price-row"><span>Full Arms</span><span>$160</span><span>$864</span></div>
      <div class="price-row"><span>Underarms</span><span>$75</span><span>$405</span></div>
      <div class="price-row"><span>Lower Legs</span><span>$120</span><span>$800</span></div>
      <div class="price-row"><span>Full legs</span><span>$300</span><span>$1620</span></div>
    </div>
    <div class="contact">
      <span class="pill">Contact Us</span>
      <svg class="pin" viewBox="0 0 14 14"><circle cx="7" cy="7" r="6"/><path d="M7 10.5C5 8 4.8 7 4.8 6a2.2 2.2 0 0 1 4.4 0c0 1-.2 2-2.2 4.5Z"/></svg>
      <p>2180 W. Cedar Lane, Suite 14<br>Glendale, AZ 85300</p>
      <p><svg viewBox="0 0 10 10"><circle cx="5" cy="5" r="4"/></svg>(602) 555-0148</p>
      <p><svg viewBox="0 0 10 10"><rect x="1" y="2" width="8" height="6"/><path d="M1 2l4 3 4-3"/></svg>welcome@quenvoraspaandwellness.com</p>
      <p><svg viewBox="0 0 10 10"><circle cx="5" cy="5" r="4"/><path d="M1 5h8M5 1c2 2 2 6 0 8M5 1c-2 2-2 6 0 8"/></svg>www.quenvoraspaandwellness.com</p>
    </div>
    <div class="base-strip"></div>
  </article>

  <article class="panel panel--cover">
    <svg class="cover-art" viewBox="0 0 280 575">
      <defs>
        <linearGradient id="gc" x1="0" y1="0" x2="1" y2="1"><stop offset="0" stop-color="#b8901f"/><stop offset=".5" stop-color="#e2c04a"/><stop offset="1" stop-color="#c59d27"/></linearGradient>
        <radialGradient id="gp" cx=".4" cy=".4"><stop offset="0" stop-color="#f5f3ef"/><stop offset=".6" stop-color="#d9d7d2"/><stop offset="1" stop-color="#a9a7a2"/></radialGradient>
        <radialGradient id="gf" cx=".5" cy=".45"><stop offset="0" stop-color="#f3dccb"/><stop offset="1" stop-color="#b88a6c"/></radialGradient>
      </defs>
      <path d="M0 575V330Q40 430 150 430Q250 420 280 330V575Z" fill="url(#gc)"/>
      <circle cx="160" cy="300" r="120" fill="url(#gc)"/>
      <circle cx="165" cy="285" r="108" fill="var(--mint)"/>
      <circle cx="165" cy="285" r="103" fill="url(#gp)" role="img" aria-label="Spa still life photo: smooth grey stones, white lily and cream jar on a plate"/>
      <circle cx="80" cy="170" r="44" fill="var(--mint)"/>
      <circle cx="80" cy="170" r="40" fill="url(#gf)" role="img" aria-label="Portrait photo of a smiling woman touching her cheek"/>
    </svg>
    <div class="cover-brand">
      <div class="name">Marrow<span class="dot"></span></div>
      <div class="sub">Medical Spa &amp; Wellness</div>
    </div>
    <p class="cover-tag">Prioritize Your<br>Health &amp; Wellness.</p>
    <p class="cover-url">www.quenvoraspaandwellness.com</p>
  </article>
</section>

<section class="sheet sheet--inside">

  <article class="panel panel--aesthetics">
    <div class="inner">
      <div class="rate"><span class="tab tab--gold">Smoothline</span><b>$10/ per unit</b></div>
      <div class="rate"><span class="tab tab--gold">Relaxa</span><b>$4/ per unit</b></div>
      <p class="fillers">FILLERS- BOOK FOR FREE CONSULTATION</p>
      <div class="needle"><span>Micro needling pen</span><span>$250 face<br>$250 decolletage<br>$50 add neck<br>$150 add PRP<br>$175 add stem cells</span></div>
      <span class="section-tab">Lumen Peel</span>
      <div class="item"><span>Lumen Peel Classic. Great, general first-time peel for all ages and skin concerns.</span><span class="price">$225</span></div>
      <div class="item"><span>Lumen Peel Renew. This peel penetrates deeper to combat the signs of aging, soften fine lines and wrinkles, and enhance collagen stimulation to increase cell turnover and help firm the skin.</span><span class="price">$250</span></div>
      <div class="item"><span>Lumen Peel Clear. Helpful in treating acne. This is a multi-faceted treatment for the many triggers and symptoms of acne, from dead skin cells and excessive oiliness to clogged pores and all types of blemishes.</span><span class="price">$250</span></div>
      <div class="item"><span>Lumen Peel Even Tone. Works to suppress the production of melanin while promoting rapid cell turnover for more even and bright skin tone.</span><span class="price">$265</span></div>
      <div class="item"><span>Lumen Peel Body. Similar treatment as the Even Tone Peel, but uniquely formulated for the body.</span><span class="price">$375</span></div>
      <div class="bar">
        <span class="pill">PRP for hair restoration- book for free consultation</span>
        <span class="pill">Sclerotherapy- book for free consultation</span>
      </div>
    </div>
    <div class="base-strip"></div>
  </article>

  <article class="panel panel--injectables">
    <div class="inner">
      <span class="section-tab" style="margin-top:0">Injectables</span>
      <div class="line"><span>Vitamin B12 Injection</span><span class="price">$30</span></div>
      <div class="line"><span>MIC (Methionine, Inisitol, Choline) Injection</span><span class="price">$30</span></div>
      <div class="line"><span>Amino Blend Injection</span><span class="price">$30</span></div>
      <div class="line"><span>Vitamin B Complex Injection<br>(Vitamins B1, B2, B3, B5 and B6)</span><span class="price">$30</span></div>
      <div class="line"><span>Glutathione Injection</span><span class="price">$30</span></div>
      <div class="line"><span>Tri-Immune Boost Injection<br>To help boost your immune system<br>-Mixture of glutathione, Vitamin C and Zinc</span><span class="price">$40</span></div>
      <span class="section-tab">IV Therapy Options:</span>
      <div class="iv-block"><ul><li>Normal Saline</li><li>-For rehydration</li></ul><span class="price">$100</span></div>
      <span class="section-tab small">Alleviate</span>
      <div class="iv-block"><ul><li>-Helps with fatigue, concentration, and insomnia</li><li class="sub">-Calcium chloride</li><li class="sub">-Magnesium</li><li class="sub">-Vitamin B12</li><li class="sub">-Blend of Vitamins B1, B2, B3, and B5</li></ul><span class="price">$220</span></div>
      <span class="section-tab small">Brainstorm</span>
      <div class="iv-block"><ul><li>-Helps with cognition</li><li class="sub">-Folic acid with B12</li><li class="sub">-L-taurine</li><li class="sub">-Alpha-Lipoic-Acid</li></ul><span class="price">$180</span></div>
      <span class="section-tab small">Get Up and Go</span>
      <div class="iv-block"><ul><li>-Helps increase energy levels</li><li class="sub">-Amino blend</li><li class="sub">-Blend of Vitamins B1, B2, B3, and B5</li></ul><span class="price">$170</span></div>
      <span class="section-tab small">Immunity</span>
      <div class="iv-block"><ul><li>-Helps increase immune defense</li><li class="sub">-Vitamin C</li><li class="sub">-Blend of Vitamins B1, B2, B3, and B5</li><li class="sub">-Zinc chloride</li></ul><span class="price">$185</span></div>
    </div>
    <div class="base-strip"></div>
  </article>

  <article class="panel panel--iv">
    <div class="inner">
      <span class="section-tab small" style="margin-top:0">Inner Beauty</span>
      <div class="iv-block"><ul><li>-Helps fortify skin, hair and nails</li><li class="sub">-Vitamin C</li><li class="sub">-Blend of Vitamins B1, B2, B3, and B5</li><li class="sub">-Biotin</li></ul><span class="price">$195</span></div>
      <span class="section-tab small">Quench</span>
      <div class="iv-block"><ul><li>-Helps rehydrate the body</li><li class="sub">-Vitamin C</li><li class="sub">-Blend of Vitamins B1, B2, B3, and B5</li><li class="sub">-Blend of Magnesium, Zinc, Manganese, Copper and Selenium</li></ul><span class="price">$195</span></div>
      <span class="section-tab small">Reboot</span>
      <div class="iv-block"><ul><li>-Helps treat hangover symptoms</li><li class="sub">-Ondavex</li><li class="sub">-Blend of Vitamins B1, B2, B3, and B5</li><li class="sub">-Blend of Magnesium, Zinc, Manganese, Copper and Selenium</li></ul><span class="price">$195</span></div>
      <span class="section-tab small">Recovery and Performance</span>
      <div class="iv-block"><ul><li>-Helps improve recovery and performance</li><li class="sub">-Vitamin C</li><li class="sub">-Amino blend</li><li class="sub">-Blend of Vitamins B1, B2, B3, and B5</li><li class="sub">-Blend of Magnesium, Zinc, Manganese, Copper and Selenium</li></ul><span class="price">$199</span></div>
      <span class="section-tab small">Classic Cocktail</span>
      <div class="iv-block"><div><p>-Helps boost the immune system and in treating a hangover</p>
        <div class="two-col"><ul><li class="sub">-Magnesium Chloride</li><li class="sub">-Dexpanthenol</li><li class="sub">-Vitamin B1</li><li class="sub">-Riboflavin-5-phosphate</li><li class="sub">-Vitamin B6</li></ul><ul><li>-Vitamin B3</li><li>-Calcium Gluconate</li><li>-Vitamin B12</li><li>-Vitamin C</li></ul></div></div><span class="price">$250</span></div>
    </div>
    <div class="base-strip"></div>
  </article>
</section>

</body>
</html>
```